Wesbite design for Investment Firm

We want a basic (clean) website that follows the form, fonts and colors of our attachments. This is for a financial investment management firm, but we have a boutique (anti-Wall Street) approach. Site should have an Home Page (Logo up top - room for basic copy on bottom, Philosophy Page (room for Quarterly Letter attachment and basic copy, Performance Page (room for Performance Overview and Performance Analysis and basic copy), Team Page, Commentary Page and Contact
Updates

Reason: Some designers have asked for an extension. Again, please only use image of Train Station or Train Station Logo in design.

Target Market(s)

Small and mid-size financial advisors from across the country

Industry/Entity Type

Financial

Number of Pages Required

5+ page

Font styles to use
Other font styles liked:
• Palotino Linotype

Colors
3176b5
cfdeed
ffffff

Requirements
Must have
• Please refer to existing site www.qorvenbay.com. Of note, this is too complex / cluttered. We simply want Blur, Grey and White consistent with attachments. The copy is pretty good, but will be simplified (and no quotes)
Should not have
• No images other than train station logo and / or train station image

```html
<!DOCTYPE html>
<html lang="en">
<head>
<meta charset="utf-8">
<title>Alder Crest Investment Company</title>
<link rel="stylesheet" href="https://fonts.googleapis.com/css2?family=Roboto+Slab:wght@400;700&family=Poppins:ital,wght@0,400;0,500;0,600;0,700;1,400&display=swap">
<style>
:root{
  --blue:#3176b5;
  --blue-dark:#1f4f86;
  --navy:#163d6b;
  --pale:#cfdeed;
  --white:#ffffff;
  --grey-bg:#eeeeee;
  --ink:#222a33;
  --text:#555c66;
  --muted:#8a9099;
}
*{margin:0;padding:0;box-sizing:border-box}
html,body{width:1200px;height:3226px;overflow:hidden}
body{position:relative;background:var(--white);font-family:'Poppins',sans-serif;color:var(--text)}
.abs{position:absolute}
.slab{font-family:'Roboto Slab',serif}

/* hero */
.hero{left:0;top:0;width:1200px;height:555px;background:linear-gradient(160deg,#25476f 0%,#1b3658 55%,#284f7c 100%)}
.brand{left:172px;top:12px;color:var(--white);font-family:'Roboto Slab',serif;font-size:22px}
.brand-sub{left:172px;top:40px;color:#4c9be2;font-size:10.5px;font-weight:600;letter-spacing:.3px}
.nav{left:570px;top:24px;display:flex;gap:15px;font-size:10.5px;font-weight:500;color:var(--white)}
.nav .on{border-bottom:1px solid var(--white);padding-bottom:2px}
.hero-title{left:0;width:1200px;top:210px;text-align:center;color:var(--white);font-family:'Roboto Slab',serif;font-size:40px}
.hero-text{left:300px;width:600px;top:274px;text-align:center;color:var(--white);font-size:12px;line-height:20px}
.btn{display:flex;align-items:center;justify-content:center;font-size:11px;font-weight:600;letter-spacing:1px}
.btn-light{left:445px;top:344px;width:160px;height:43px;background:var(--pale);color:var(--navy)}
.btn-blue{left:605px;top:344px;width:150px;height:43px;background:var(--blue);color:var(--white)}
.dots{left:572px;top:514px;display:flex;gap:6px;align-items:center}
.dots i{display:block;width:11px;height:11px;border-radius:50%;background:#9fb3c9}
.dots i.on{width:17px;height:17px;background:var(--white)}

/* section headings */
.bracket-top{width:60px;height:30px;border-top:3px solid var(--blue);border-left:3px solid var(--blue)}
.bracket-bot{width:60px;height:14px;border-bottom:3px solid var(--blue);border-left:3px solid var(--blue)}
.sec-title{font-family:'Roboto Slab',serif;font-size:28px;color:var(--ink)}

/* offer */
.offer{left:0;top:555px;width:1200px;height:450px;background:var(--grey-bg)}
.arrows{left:998px;top:636px;display:flex;gap:8px}
.feature{width:220px;text-align:center}
.diamond{width:58px;height:58px;background:var(--blue);transform:rotate(45deg);margin:0 auto;display:flex;align-items:center;justify-content:center}
.diamond svg{transform:rotate(-45deg)}
.feature h3{font-family:'Roboto Slab',serif;font-weight:400;font-size:14px;color:var(--blue);margin-top:34px}
.feature p{font-size:10.5px;line-height:15px;color:var(--text);margin-top:8px;padding:0 10px}

/* company band */
.company{left:0;top:946px;width:1200px;height:482px;background:linear-gradient(180deg,#3567a0 0%,#24507f 100%);clip-path:polygon(0 46px,1200px 0,1200px 482px,0 482px)}
.co-title{left:172px;top:1025px;color:var(--white);font-family:'Roboto Slab',serif;font-size:18px}
.co-text{left:172px;width:420px;color:#e6eef7;font-size:11.5px;line-height:21px}
.btn-outline{left:172px;top:1302px;width:158px;height:44px;border:2px solid var(--white);color:var(--white)}
.letter-title{left:682px;top:1022px;color:var(--white);font-family:'Roboto Slab',serif;font-size:18px}
.letter{left:682px;top:1078px;width:345px;height:298px;background:var(--white);text-align:center;font-family:'Roboto Slab',serif;color:#4a4f57}
.letter .sketch{width:120px;height:62px;margin:26px auto 0;background:#e4e6ea}
.letter .l1{font-size:7.5px;letter-spacing:1.5px;margin-top:20px}
.letter .l2{font-size:5.5px;letter-spacing:1px;margin-top:4px;color:var(--muted)}
.letter .l3{font-size:7px;letter-spacing:1.5px;margin-top:22px;font-weight:700}
.letter .l4{font-size:5.5px;margin-top:22px;color:var(--muted)}
.letter .l5{font-size:5px;margin-top:32px;color:var(--muted);line-height:9px}

/* why */
.why-photo-top{left:172px;top:1634px;width:344px;height:228px;background:linear-gradient(160deg,#6e8fb8,#2f5f96)}
.why-photo-bot{left:172px;top:1872px;width:344px;height:236px;background:linear-gradient(160deg,#4a74a8,#244d80)}
.why-frame{left:200px;top:1660px;width:262px;height:400px;border:3px solid rgba(255,255,255,.75)}
.why-box{left:322px;top:1785px;width:258px;height:176px;background:var(--navy);border:4px solid var(--white);display:flex;flex-direction:column;align-items:center;justify-content:center;color:var(--white);font-family:'Poppins',sans-serif;font-weight:600;font-size:20px;letter-spacing:2.5px;line-height:37px}
.why-lead{left:612px;top:1565px;font-family:'Roboto Slab',serif;font-size:22px;color:var(--blue)}
.why-lead b{color:var(--navy)}
.why-text{left:612px;width:420px;font-size:11.5px;line-height:20px;font-style:italic;color:var(--text)}

/* stats */
.stats{left:0;top:2176px;width:1200px;height:276px;background:linear-gradient(170deg,#4b86c6,#2f6aac)}
.stat{width:200px;text-align:center;color:var(--white)}
.stat .num{font-family:'Roboto Slab',serif;font-size:40px;margin-top:18px;line-height:44px}
.stat .lbl{font-weight:600;font-size:17px;letter-spacing:.3px}

/* blog + testimonials */
.col-title{font-family:'Roboto Slab',serif;font-size:24px;color:var(--blue);letter-spacing:.3px}
.col-rule{width:48px;height:3px;background:var(--navy)}
.post-img{left:172px;top:2582px;width:415px;height:292px;background:linear-gradient(150deg,#7394bd,#2c5a91)}
.post-date{left:172px;top:2582px;width:66px;height:64px;background:var(--blue);color:var(--white);text-align:center}
.post-date b{display:block;font-size:32px;font-weight:600;line-height:42px}
.post-date span{font-size:8px;display:block;margin-top:-4px}
.post-card{left:190px;top:2818px;width:400px;height:64px;background:var(--white);padding:12px 14px}
.post-card h4{font-size:13px;font-weight:600;color:var(--ink)}
.post-card p{font-size:9.5px;line-height:15px;color:var(--text);margin-top:10px}
.btn-small{left:200px;top:2906px;width:95px;height:28px;background:var(--blue);color:var(--white);font-size:9.5px;letter-spacing:.5px}
.testi{left:612px;top:2585px;width:415px;height:335px;border:3px solid #e2e4e8;text-align:center}
.testi .q{font-family:'Roboto Slab',serif;font-size:62px;color:var(--blue);line-height:1;margin-top:44px;font-weight:700}
.testi p{font-size:12px;line-height:23px;color:var(--text);padding:0 50px;margin-top:14px}
.testi .who{font-size:12px;color:var(--blue);margin-top:10px;font-weight:500}
.avatar{background:#dfe3e8;border:3px solid var(--white);box-shadow:0 0 0 1px #d6d9de}

/* footer */
.footer{left:0;top:3006px;width:1200px;height:220px;background:var(--blue)}
.social{left:548px;top:3055px;display:flex;gap:10px}
.social i{display:block;width:47px;height:47px;border-radius:50%;border:2px solid var(--white)}
.foot-links{left:0;width:1200px;top:3124px;text-align:center;color:var(--white);font-size:9.5px;font-weight:600;word-spacing:2px}
.foot-links span{margin:0 10px}
.copy{left:0;width:1200px;top:3145px;text-align:center;color:var(--white);font-size:9px}
</style>
</head>
<body>

<!-- hero -->
<div class="abs hero" role="img" aria-label="Desk scene with laptop, coffee and financial papers under a blue tint"></div>
<div class="abs brand">Alder Crest Investment Company</div>
<div class="abs brand-sub">SEPARATELY MANAGED ACCOUNTS</div>
<nav class="abs nav"><span class="on">HOME</span><span>PHILOSOPHY</span><span>PERFORMANCE</span><span>TEAM</span><span>LETTERS</span><span>COMMENTARY</span><span>CONTACT</span></nav>
<h1 class="abs hero-title">We Support Your Financial Interest</h1>
<p class="abs hero-text">Lorem Ipsum is simply dummy text of the printing and typesetting industry. Lorem Ipsum has been the industry's standard dummy text ever since the 1500s</p>
<a class="abs btn btn-light">OUR COMPANY</a>
<a class="abs btn btn-blue">GET IN TOUCH</a>
<div class="abs dots"><i></i><i class="on"></i><i></i></div>

<!-- what we offer -->
<section class="abs offer"></section>
<div class="abs bracket-top" style="left:172px;top:600px"></div>
<h2 class="abs sec-title" style="left:172px;top:628px">What we offer</h2>
<div class="abs bracket-bot" style="left:172px;top:670px"></div>
<div class="abs arrows">
  <svg width="12" height="14" viewBox="0 0 12 14"><path d="M9 1 3 7l6 6" fill="none" stroke="#555" stroke-width="1.5"/></svg>
  <svg width="12" height="14" viewBox="0 0 12 14"><path d="M3 1l6 6-6 6" fill="none" stroke="#555" stroke-width="1.5"/></svg>
</div>

<div class="abs feature" style="left:161px;top:745px">
  <div class="diamond"><svg width="30" height="30" viewBox="0 0 30 30" fill="none" stroke="#fff" stroke-width="1.6"><rect x="5" y="14" width="6" height="12"/><rect x="12" y="8" width="6" height="18"/><rect x="19" y="11" width="6" height="15"/></svg></div>
  <h3>Audit &amp; Assurance</h3>
  <p>Lorem Ipsum is simply dummy text of the printing and typesetting industry. Lorem Ipsum has...</p>
</div>
<div class="abs feature" style="left:380px;top:745px">
  <div class="diamond"><svg width="30" height="30" viewBox="0 0 30 30" fill="none" stroke="#fff" stroke-width="1.6"><rect x="4" y="6" width="22" height="15"/><path d="M8 17l5-5 4 3 5-6M15 21v4M10 25h10"/></svg></div>
  <h3>Business Services</h3>
  <p>Lorem Ipsum is simply dummy text of the printing and typesetting industry. Lorem Ipsum has...</p>
</div>
<div class="abs feature" style="left:600px;top:745px">
  <div class="diamond"><svg width="30" height="30" viewBox="0 0 30 30" fill="none" stroke="#fff" stroke-width="1.6"><path d="M4 15a11 9 0 0 1 22 0zM15 15v9a2 2 0 0 1-4 0"/></svg></div>
  <h3>IT Control Solutions</h3>
  <p>Lorem Ipsum is simply dummy text of the printing and typesetting industry. Lorem Ipsum has...</p>
</div>
<div class="abs feature" style="left:819px;top:745px">
  <div class="diamond"><svg width="30" height="30" viewBox="0 0 30 30" fill="none" stroke="#fff" stroke-width="1.6"><rect x="4" y="10" width="18" height="12"/><path d="M7 10V7h18v12h-3"/><circle cx="13" cy="16" r="3"/></svg></div>
  <h3>Tax Advisory Services</h3>
  <p>Lorem Ipsum is simply dummy text of the printing and typesetting industry. Lorem Ipsum has...</p>
</div>

<!-- company band -->
<section class="abs company" role="img" aria-label="Historic train station building under a blue tint"></section>
<h2 class="abs co-title">ALDER CREST INVESTMENT COMPANY</h2>
<p class="abs co-text" style="top:1073px">We founded Alder Crest Investment Company in 1999, initially managing wealth from our family and friends in the town of Alder Crest. The high expectations of our original investors is a key contributor to our value driven investment philosophy.</p>
<p class="abs co-text" style="top:1178px">Based in Marlow, TX, we manage assets for both individuals and institutions. Our investment methodology stresses absolute returns vs. relative performance, blending a combination of fundamental analysis, discipline and patience with the goal of preserving and compounding capital.</p>
<a class="abs btn btn-outline">READ MORE</a>
<h2 class="abs letter-title">INVESTMENT ADVISER'S LETTER</h2>
<div class="abs letter">
  <div class="sketch" role="img" aria-label="Pencil sketch of the train station"></div>
  <div class="l1">ALDER CREST INVESTMENT COMPANY</div>
  <div class="l2">PERSONAL PORTFOLIO MANAGEMENT</div>
  <div class="l3">INVESTMENT ADVISER'S LETTER</div>
  <div class="l4">JULY 2017</div>
  <div class="l5">www.qorvenbay.com<br>100 MAIN STREET, SUITE 10<br>MARLOW, TEXAS</div>
</div>

<!-- why choose us -->
<div class="abs bracket-top" style="left:570px;top:1482px"></div>
<h2 class="abs sec-title" style="left:0;width:1200px;text-align:center;top:1510px">Why choose us</h2>
<div class="abs bracket-bot" style="left:570px;top:1552px"></div>

<div class="abs why-photo-top" role="img" aria-label="Team meeting around a conference table, blue tinted"></div>
<div class="abs why-photo-bot" role="img" aria-label="Tablet showing financial charts, blue tinted"></div>
<div class="abs why-frame"></div>
<div class="abs why-box"><span>TODAY</span><span>TOMORROW</span><span>TOGETHER</span></div>

<div class="abs why-lead">Let <b>tomorrow</b> begin <b>today.</b></div>
<p class="abs why-text" style="top:1668px">Temporibus autem quibusdam et aut officiis debitis is aut rerum necessitatibus saepes eveniet ut etes seo lage voluptates repu dian dae sint et molestiae non mes for Creating.</p>
<p class="abs why-text" style="top:1750px">Temporibus autem quibusdam et aut officiis debitis is aut rerum necessitatibus saepes eveniet ut etes seo lage voluptates repu dian dae sint et molestiae non mes for Creating.</p>

<div class="abs feature" style="left:610px;top:1858px">
  <div class="diamond"><svg width="30" height="30" viewBox="0 0 30 30" fill="none" stroke="#fff" stroke-width="1.6"><path d="M9 5h12v6a6 6 0 0 1-12 0zM9 8H5a4 4 0 0 0 4 5M21 8h4a4 4 0 0 1-4 5M15 17v5M10 25h10"/></svg></div>
  <h3>Professhional</h3>
  <p>Lorem Ipsum is simply dummy text of the printing and typesetting industry. Lorem Ipsum has...</p>
</div>
<div class="abs feature" style="left:819px;top:1858px">
  <div class="diamond"><svg width="30" height="30" viewBox="0 0 30 30" fill="none" stroke="#fff" stroke-width="1.6"><rect x="4" y="10" width="22" height="15"/><path d="M11 10V6h8v4M4 16h22"/></svg></div>
  <h3>Experienced</h3>
  <p>Lorem Ipsum is simply dummy text of the printing and typesetting industry. Lorem Ipsum has...</p>
</div>

<!-- stats -->
<section class="abs stats" role="img" aria-label="Desk with glasses, notebook, calculator and charts under a blue tint"></section>
<div class="abs stat" style="left:170px;top:2218px">
  <svg width="46" height="40" viewBox="0 0 46 40" fill="none" stroke="#fff" stroke-width="2"><rect x="4" y="11" width="38" height="25"/><path d="M16 11V5h14v6M4 21h38"/></svg>
  <div class="num">947</div><div class="lbl">PROJECTS</div>
</div>
<div class="abs stat" style="left:390px;top:2218px">
  <svg width="46" height="40" viewBox="0 0 46 40" fill="none" stroke="#fff" stroke-width="2"><circle cx="23" cy="12" r="7"/><path d="M10 38c0-9 6-15 13-15s13 6 13 15"/></svg>
  <div class="num">867</div><div class="lbl">CLIENT'S</div>
</div>
<div class="abs stat" style="left:610px;top:2218px">
  <svg width="46" height="40" viewBox="0 0 46 40" fill="none" stroke="#fff" stroke-width="2"><path d="M15 3h16v10a8 8 0 0 1-16 0zM15 7H8a6 6 0 0 0 7 8M31 7h7a6 6 0 0 1-7 8M23 21v8M15 37h16"/></svg>
  <div class="num">150</div><div class="lbl">AWARD'S</div>
</div>
<div class="abs stat" style="left:829px;top:2218px">
  <svg width="46" height="40" viewBox="0 0 46 40" fill="none" stroke="#fff" stroke-width="2"><path d="M10 4l8 2-3 12a5 5 0 0 1-9-2zM12 20l-3 14M5 36h8M36 4l-8 2 3 12a5 5 0 0 0 9-2zM34 20l3 14M33 36h8"/></svg>
  <div class="num">289</div><div class="lbl">DRINKS</div>
</div>

<!-- blog -->
<h2 class="abs col-title" style="left:172px;top:2505px">OUR BLOG</h2>
<div class="abs col-rule" style="left:172px;top:2550px"></div>
<div class="abs post-img" role="img" aria-label="Hands working at a laptop beside financial reports"></div>
<div class="abs post-date"><b>10</b><span>august, 2017</span></div>
<div class="abs post-card">
  <h4>CORE EQUITY PORTFOLIO – Q2 2017</h4>
  <p>Based on our estimate of fair-value relative to the company's current stock price, we determine each company's current margin of safety...</p>
</div>
<a class="abs btn btn-small">READ MORE</a>

<!-- testimonials -->
<h2 class="abs col-title" style="left:612px;top:2505px">TESTIMONIALS</h2>
<div class="abs col-rule" style="left:612px;top:2550px"></div>
<div class="abs testi">
  <div class="q">&ldquo;</div>
  <p>Lorem Ipsum is simply dummy text of the printing and typesetting industry. Lorem Ipsum has been the industry's standard dummy text ever.</p>
  <div class="who">– Anonymous</div>
</div>
<div class="abs avatar" role="img" aria-label="Client portrait" style="left:717px;top:2880px;width:52px;height:52px"></div>
<div class="abs avatar" role="img" aria-label="Client portrait" style="left:782px;top:2866px;width:80px;height:80px"></div>
<div class="abs avatar" role="img" aria-label="Client portrait" style="left:870px;top:2880px;width:52px;height:52px"></div>

<!-- footer -->
<footer class="abs footer"></footer>
<div class="abs social" aria-label="Social links"><i></i><i></i><i></i></div>
<div class="abs foot-links"><span>PERFORMANCE OVERVIEW</span>/<span>PERFORMANCE ANALYSIS</span>/<span>VERIFICATION STATEMENT</span>/<span>ALDER CREST ADV PART 2</span></div>
<div class="abs copy">© 2017 Alder Crest Investment Company All Rights Reserved</div>

</body>
</html>
```